We are seeking two label designs for our premium pecan snack brand, TORVELLO. TORVELLO is known for its innovative pecan snacks, specifically a healthy and exotic blend of pecans, expertly salted, and infused with unique chili flavors. Our snacks are packaged in stand-up pouch bags, and we are looking for label designs product sizes - 5 oz. ( Size: 14 x 20 cm / 5.5 x 7.8 inches / Max Capacity: 16.2 oz)

Background Information:
TORVELLO is a brand committed to offering a delightful snacking experience that combines the natural richness of pecans with the bold and exotic kick of carefully selected chilies. Our snacks cater to health-conscious consumers who appreciate the fusion of premium quality, unique flavors, and nutritional goodness.

Target Market(s)

Event Attendees (Entertainment Industry), Health-Conscious Consumers

Industry/Entity Type

Entertainment (sports events, arenas, stadiums, etc)

Font styles to use
Other font styles liked:
• Brother1816 Printed

Colors

Designer to choose colors to be used in the design.

Requirements
Must have
• Nutrition Fact (attached) , TRANSPARENT PART LIKE A WINDOW TO DISPLAY THE PRODUCT

```html
<!DOCTYPE html>
<html lang="en">
<head>
<meta charset="utf-8">
<title>TORVELLO – 5 oz Pouch Label</title>
<link rel="stylesheet" href="https://fonts.googleapis.com/css2?family=Montserrat:wght@400;500;600&display=swap">
<style>
  :root {
    --backdrop: #8f8f8f;
    --pouch-white: #f7f7f7;
    --ink-dark: #262626;
    --brand-orange: #e4572e;
    --orange-deep: #cf4a24;
    --shadow-soft: rgba(0, 0, 0, 0.18);
    --pecan-brown: #8a4a25;
    --pecan-light: #b8683a;
  }
  html, body {
    margin: 0;
    padding: 0;
    width: 1200px;
    height: 1199px;
    overflow: hidden;
    background: var(--backdrop);
  }
  .canvas {
    position: relative;
    width: 1200px;
    height: 1199px;
    display: flex;
    align-items: center;
    justify-content: center;
  }
  .pouch-label {
    display: block;
    width: 560px;
    height: 1100px;
  }
  .brand-name {
    font-family: "Montserrat", sans-serif;
    font-weight: 500;
    font-size: 46px;
    letter-spacing: 2px;
    fill: var(--ink-dark);
  }
  .brand-byline {
    font-family: "Montserrat", sans-serif;
    font-weight: 400;
    font-size: 11px;
    letter-spacing: 0.5px;
    fill: var(--ink-dark);
  }
  .net-weight {
    font-family: "Montserrat", sans-serif;
    font-weight: 500;
    font-size: 22px;
    fill: var(--pouch-white);
  }
</style>
</head>
<body>
<main class="canvas">
  <svg class="pouch-label" viewBox="0 0 400 785" xmlns="http://www.w3.org/2000/svg">
    <defs>
      <clipPath id="pouch-shape">
        <rect x="0" y="0" width="400" height="785" rx="14" ry="14"/>
      </clipPath>
      <radialGradient id="product-fill" cx="45%" cy="40%" r="65%">
        <stop offset="0%" stop-color="var(--pecan-light)"/>
        <stop offset="100%" stop-color="var(--pecan-brown)"/>
      </radialGradient>
    </defs>

    <g clip-path="url(#pouch-shape)">
      <!-- pouch body -->
      <rect class="pouch-body" x="0" y="0" width="400" height="785" fill="var(--pouch-white)"/>

      <!-- top dark cap with orange swoosh -->
      <path class="top-swoosh" d="M60 0 C 70 90 150 150 240 140 C 320 130 375 80 400 40 V 90 C 360 140 300 175 230 172 C 150 168 95 140 70 105 C 95 125 140 140 200 140 C 120 120 75 70 60 0 Z" fill="var(--brand-orange)"/>
      <path class="top-cap" d="M40 0 H400 V40 C 370 95 300 130 220 128 C 130 125 65 75 40 0 Z" fill="var(--ink-dark)"/>

      <!-- bottom orange dome with dark edge -->
      <circle class="dome-shadow" cx="215" cy="770" r="305" fill="var(--ink-dark)"/>
      <circle class="dome" cx="225" cy="775" r="300" fill="var(--brand-orange)"/>

      <!-- product window -->
      <circle class="window-ring-accent" cx="190" cy="425" r="74" fill="var(--brand-orange)"/>
      <circle class="window-ring" cx="194" cy="428" r="70" fill="var(--ink-dark)"/>
      <circle class="product-window" cx="192" cy="427" r="60" fill="url(#product-fill)"
              role="img" aria-label="Transparent window showing roasted chili pecan halves"/>
    </g>

    <!-- brand -->
    <text class="brand-name" x="200" y="252" text-anchor="middle">TORVELLO</text>
    <text class="brand-byline" x="318" y="289" text-anchor="end">BY HALDEN</text>

    <!-- net weight -->
    <text class="net-weight" x="200" y="614" text-anchor="middle">5 oz</text>
  </svg>
</main>
</body>
</html>
```